Podcast Cover Art for Inspiring Fun Show

Title: The Dave R Hour

I am looking for a simple design that includes the following:

1. Picture of me (the one I attached with the background removed) on a simple background (please refer to attachments for ideas).
2. The title done in professional lettering that is easy to read and stands out on the background

Please see attached pictures for:

1) Other podcast art I like
2) Backgrounds that I like
3) A picture of me (please edit out the background)

Target Market(s)

Anyone into personal-development, inspiring content and motivational stories.

Font styles to use
Sans Serif

Colors

Designer to choose colors to be used in the design.

Requirements
Must have
• - Title "The Dave R Hour" in professional lettering that is large and very easy to read
• - Picture of me on the background

```html
<!DOCTYPE html>
<html lang="en">
<head>
<meta charset="utf-8">
<title>The Dave R Hour — Podcast Cover</title>
<link rel="stylesheet" href="https://fonts.googleapis.com/css2?family=Montserrat:wght@700&display=swap">
<style>
  :root {
    --sky-grey: #e1e0e1;
    --divider: #1d2a2e;
    --plank-teal: #5fbcc6;
    --plank-teal-deep: #4aaab5;
    --title-ink: #1d2a2e;
    --hair: #1e1c1e;
    --skin: #d9a98f;
    --jacket: #2e3440;
  }
  html, body {
    margin: 0;
    padding: 0;
    width: 1200px;
    height: 1200px;
    overflow: hidden;
    background: var(--sky-grey);
  }
  .cover {
    position: relative;
    width: 1200px;
    height: 1200px;
    overflow: hidden;
    background: var(--sky-grey);
  }
  .cover__art {
    position: absolute;
    inset: 0;
    width: 1200px;
    height: 1200px;
    display: block;
  }
  .show-title {
    position: absolute;
    left: 48px;
    top: 150px;
    margin: 0;
    font-family: "Montserrat", "Helvetica Neue", Arial, sans-serif;
    font-weight: 700;
    font-size: 124px;
    line-height: 136px;
    letter-spacing: -2px;
    color: var(--title-ink);
  }
  .show-title__line {
    display: block;
    white-space: nowrap;
  }
</style>
</head>
<body>
<main class="cover">
  <svg class="cover__art" viewBox="0 0 1200 1200" xmlns="http://www.w3.org/2000/svg">
    <defs>
      <linearGradient id="plankWall" x1="0" y1="0" x2="1" y2="0">
        <stop offset="0" stop-color="var(--plank-teal-deep)"/>
        <stop offset="0.5" stop-color="var(--plank-teal)"/>
        <stop offset="1" stop-color="var(--plank-teal-deep)"/>
      </linearGradient>
      <linearGradient id="hostTones" x1="0" y1="0" x2="0" y2="1">
        <stop offset="0" stop-color="var(--hair)"/>
        <stop offset="0.2" stop-color="#6b5046"/>
        <stop offset="0.35" stop-color="var(--skin)"/>
        <stop offset="0.68" stop-color="var(--skin)"/>
        <stop offset="0.8" stop-color="var(--jacket)"/>
        <stop offset="1" stop-color="var(--jacket)"/>
      </linearGradient>
    </defs>

    <rect class="backdrop-top" x="0" y="0" width="1200" height="598" fill="var(--sky-grey)"/>
    <rect class="backdrop-wall" x="0" y="603" width="1200" height="597" fill="url(#plankWall)"
          role="img" aria-label="Teal painted wooden plank wall"/>
    <rect class="backdrop-divider" x="0" y="598" width="1200" height="5" fill="var(--divider)"/>

    <path class="host-portrait" fill="url(#hostTones)" role="img"
          aria-label="Cut-out photo of the host smiling, wearing a grey hoodie over a checked shirt"
          d="M700 230 C700 120 820 56 960 62 C1100 68 1160 150 1160 260
             L1160 440 C1190 450 1190 560 1160 600
             C1150 700 1110 780 1060 820 L1080 860
             C1140 880 1190 900 1200 920 L1200 1200 L300 1200
             C340 1100 480 1060 600 1010 C680 980 740 930 770 880
             L760 820 C720 780 700 700 690 610
             C660 590 660 480 690 470 Z"/>
  </svg>

  <h1 class="show-title">
    <span class="show-title__line">The</span>
    <span class="show-title__line">Dave R</span>
    <span class="show-title__line">Hour</span>
  </h1>
</main>
</body>
</html>
```